Vantor - Adventurous, Fun, Exciting, Social Fitness Club needs a Webpage with attitude!

Vantor... we're a fun, social, outdoor fitness club that needs not just a homepage designed for our website, but in the process a "personality" for our unique, innovative and cheeky brand.
We pride ourselves on getting our members outdoors trying new, exciting physical activities in an effort to find joy in an active lifestyle, and sharing that experience with other like minded people. We offer:
- Personal Training (1-on-1 Fitness Training)
- Group Fitness Classes (Boxing, Pilates, etc)
- Boot Camps (Military Style - Sandbags, Ropes, Tyres, etc)
- Events (Fun Runs, Triathlons, Ocean Swims, Treks, etc)
- Adventures(Machu Picchu Trek, Rock Climbing, Kayaking, etc)
Our tag line is 'No Judgements. No Limits!' The homepage should be exciting, adventurous and innovative, illustrating the values of our brand: possibility, thirst for life, personal accomplishment & freedom. It should be fun, friendly & inviting.
A few of our key benefits to members are:
- No Boring Workouts
- No Joining Fees or Long Term Contracts
- Results Guaranteed
The links below should give you a rough idea of the sort of "feel" we're after (vibrant, active, adventurous ).
http://www.pupiljourneys.com.au/
http://www.layoutgoblin.com/website-templates/31924.html
http://www.layoutgoblin.com/website-templates/32751.html
http://www.pivel.com/
Target Market(s)
Real, Everyday People - Men & Women (30:70) aged mainly between 21-40, who want a more exciting and enjoyable fitness experience than your typical gym offers.
Industry/Entity Type
Fitness
Requirements
Must have
- Strong, uplifting and motivating images of people enjoying fitness/physical activities outdoors

```html
<!DOCTYPE html>
<html lang="en">
<head>
<meta charset="utf-8">
<title>Vantor — No Judgements. No Limits!</title>
<link rel="stylesheet" href="https://fonts.googleapis.com/css2?family=Alegreya+Sans+SC:wght@500&family=Black+Ops+One&family=Lora:ital@1&family=Maven+Pro:wght@400;500;700&family=Oswald:wght@300;400&family=Rubik+Dirt&family=Special+Elite&family=Squada+One&display=swap">
<style>
:root{
  --orange-deep:#e35c0b;
  --orange:#ee7a16;
  --orange-light:#f59a2c;
  --yellow:#f6cf1c;
  --yellow-light:#fde45c;
  --sky:#d6e6f0;
  --charcoal:#3e3f46;
  --charcoal-dark:#2e2f35;
  --red:#d3101a;
  --purple:#7a2a8c;
  --brown:#6a4c34;
  --cream:#efe9d6;
  --ink:#4a3a22;
  --white:#ffffff;
}
*{box-sizing:border-box;margin:0;padding:0}
html,body{width:1200px;height:1186px;overflow:hidden}
body{position:relative;background:var(--sky);font-family:"Maven Pro",sans-serif}
.abs{position:absolute}

/* header */
.site-header{left:0;top:0;width:1200px;height:148px;background:var(--orange-deep)}
.header-inner{left:76px;top:0;width:1024px;height:148px;background:linear-gradient(180deg,var(--orange-light),var(--orange) 60%,#f08a20)}
.brand{left:52px;top:36px;display:flex;align-items:center;gap:10px}
.brand-dot{width:26px;height:26px;border-radius:50%;background:var(--yellow-light)}
.brand-name{font-family:"Maven Pro",sans-serif;font-weight:700;font-size:52px;color:var(--yellow-light);letter-spacing:1px}
.tagline{left:66px;top:122px;font-family:"Maven Pro",sans-serif;font-weight:500;font-size:15px;color:#1a1a1a}
.call{left:776px;top:12px;font-family:"Oswald",sans-serif;font-size:24px;color:var(--white)}
.call b{color:var(--yellow-light);font-weight:400;font-size:20px;margin-right:6px;letter-spacing:1px}
.util-nav{left:657px;top:54px;width:336px;height:28px;background:var(--red);border:1px dashed #fff3;display:flex;align-items:center;justify-content:space-around;font-family:"Oswald",sans-serif;font-size:15px;color:var(--white);letter-spacing:.5px}
.util-nav span+span{border-left:1px solid #fff8;padding-left:12px}

/* main nav */
.main-nav{left:0;top:148px;width:1200px;height:57px;background:linear-gradient(180deg,var(--yellow-light),var(--yellow));display:flex;align-items:center;padding-left:157px;gap:0}
.main-nav a{font-family:"Alegreya Sans SC",sans-serif;font-size:24px;color:#4a4a4a;text-decoration:none}

/* hero */
.hero{left:100px;top:205px;width:1000px;height:373px;background:var(--orange)}
.slide{left:35px;top:16px;width:558px;height:342px;border:4px solid var(--white);box-shadow:0 2px 8px #0006;background:linear-gradient(160deg,#9aa0a4,#6e7479 35%,#c9ced2 60%,#b33a2c 85%,#7a1e18)}
.slide-title{right:10px;top:18px;text-align:right;font-family:"Rubik Dirt",sans-serif;color:#555}
.slide-title .t1{font-size:36px;letter-spacing:2px}
.slide-title .t2{font-size:25px;margin-right:10px}
.slide-quote{left:344px;top:96px;width:210px;font-family:"Lora",serif;font-style:italic;font-size:15px;line-height:24px;color:var(--white)}
.slide-quote .by{display:block;text-align:right;margin-right:4px}
.dots{left:10px;top:316px;display:flex;gap:11px}
.dots i{width:18px;height:18px;border-radius:50%;background:var(--red)}
.dots i:first-child{background:var(--cream)}

.ribbon{left:620px;top:20px}
.ribbon-text{left:672px;top:23px;width:240px;text-align:center;font-family:"Oswald",sans-serif;font-size:29px;color:var(--white);letter-spacing:1px}
.offer-frame{left:610px;top:72px;width:362px;height:215px;background:var(--charcoal);border-radius:8px}
.offer-photo{left:638px;top:80px;width:304px;height:197px;border:3px solid var(--white);background:linear-gradient(120deg,#2f69b8,#7fb0e0 50%,#b69a74 75%,#8a6d4e)}
.offer-badge{left:726px;top:182px;width:52px;height:52px;border-radius:50%;background:#8fc23f}
.offer-text{left:646px;top:202px;width:292px;text-align:right;font-family:"Squada One",sans-serif;font-size:28px;line-height:30px;color:var(--yellow-light);text-shadow:1px 1px 0 #3a2a00}
.arrow{top:150px;width:30px;height:44px;background:#ddd;display:flex;align-items:center;justify-content:center}
.arrow.l{left:610px;border-radius:22px 0 0 22px}
.arrow.r{left:942px;border-radius:0 22px 22px 0}
.value{left:906px;top:280px;width:46px;height:32px;border-radius:0 0 20px 20px;background:var(--charcoal-dark);color:#ddd;font-size:10px;text-align:center;line-height:11px;padding-top:5px;font-weight:700}
.join-form label{font-family:"Oswald",sans-serif;font-weight:300;font-size:18px;color:var(--white);letter-spacing:1px}
.join-form .field{width:96px;height:22px;background:#f6b07a;border:1px solid #9a4a10}
.join-btn{left:840px;top:320px;width:90px;height:38px;background:var(--charcoal);border-radius:4px;color:#eee;font-family:"Oswald",sans-serif;font-weight:300;font-size:15px;display:flex;align-items:center;justify-content:center;box-shadow:0 3px 4px #0005}

/* promo band */
.promos{left:100px;top:578px;width:1000px;height:257px;background:var(--yellow)}
.card-pt{left:33px;top:24px;width:284px;height:210px;background:var(--purple);border:4px solid var(--white);box-shadow:2px 3px 6px #0005;transform:rotate(-1deg)}
.card-pt h3{position:absolute;left:16px;top:14px;font-family:"Special Elite",serif;font-size:32px;line-height:30px;color:var(--white);font-weight:400}
.card-pt .figure{left:14px;top:84px;width:140px;height:110px;border-radius:6px;background:linear-gradient(135deg,#b04a3a,#e3b08a 60%,#9a5bb0)}
.card-pt p{position:absolute;right:12px;top:80px;width:140px;text-align:right;font-family:"Squada One",sans-serif;font-size:19px;line-height:20px;color:var(--yellow-light)}
.card-pt .unl{position:absolute;right:12px;bottom:6px;font-family:"Squada One",sans-serif;font-size:16px;color:var(--white)}
.card-gf{left:350px;top:24px;width:295px;height:206px;background:var(--cream);border:3px solid var(--red);border-radius:4px}
.card-gf h3{position:absolute;left:16px;top:10px;font-family:"Black Ops One",sans-serif;font-size:36px;line-height:34px;color:var(--red);font-weight:400}
.gf-pass{left:40px;top:94px;width:212px;height:84px;background:linear-gradient(90deg,#f4d73a,#f8e26a,#f4d73a);display:flex;flex-direction:column;align-items:center;justify-content:center;font-family:"Squada One",sans-serif;color:var(--ink);font-size:26px;line-height:28px}
.gf-pass b{font-size:30px;font-weight:400}
.card-bc{left:665px;top:24px;width:306px;height:208px;background:var(--brown);border:4px solid #f4f1ea;border-radius:10px 4px 12px 6px}
.bc-soon{right:26px;top:22px;text-align:right;font-family:"Squada One",sans-serif;font-size:22px;line-height:20px;color:var(--yellow)}
.bc-soon small{font-size:16px;display:block}
.bc-icon{top:66px;width:44px;height:44px;border-radius:50%;border:5px solid #eee}
.bc-title{left:22px;top:126px;font-family:"Black Ops One",sans-serif;font-size:44px;color:var(--white)}

/* about */
.about{left:100px;top:835px;width:1000px;height:290px;background:var(--charcoal)}
.about h2{position:absolute;left:23px;top:24px;font-weight:500;font-size:23px;color:#efe8d8;letter-spacing:.5px}
.about-copy{left:23px;top:70px;width:605px;font-size:13.5px;line-height:18px;color:var(--white);text-align:justify}
.about-copy p+p{margin-top:18px}
.video{left:661px;top:13px;width:318px;height:264px;background:#1f6fb0;border:3px solid #2c87c9;padding:4px}
.video-frame{width:100%;height:230px;background:linear-gradient(110deg,#cfcfcf,#8a8a8a 40%,#e6e0d8 55%,#555 80%,#2a2a2a)}
.play{left:130px;top:96px;width:52px;height:36px;border-radius:6px;background:#ccccccd0;display:flex;align-items:center;justify-content:center}
.controls{left:4px;bottom:4px;width:302px;height:20px;background:linear-gradient(#eaf4fb,#9cc3e0);display:flex;align-items:center;gap:6px;padding:0 6px;font-size:8px;color:#234}
.bar{flex:1;height:5px;background:#6b8aa3;border-radius:3px}

.site-footer{left:0;top:1125px;width:1200px;height:61px;background:var(--orange-deep)}
</style>
</head>
<body>

<header class="site-header abs">
  <div class="header-inner abs">
    <div class="brand abs"><span class="brand-dot"></span><span class="brand-name">Vantor</span></div>
    <div class="tagline abs">No Judgements. No Limits!</div>
    <div class="call abs"><b>CALL US</b>1300 555 014</div>
    <nav class="util-nav abs"><span>TIMETABLE</span><span>CLUB LOCATIONS</span><span>LOGIN</span></nav>
  </div>
</header>

<nav class="main-nav abs">
  <a style="width:140px">Home</a>
  <a style="width:178px">About Us</a>
  <a style="width:155px">Fitness</a>
  <a style="width:307px">Evenets and Adventures</a>
  <a>Contact us</a>
</nav>

<section class="hero abs">
  <div class="slide abs" role="img" aria-label="Kayakers paddling through white water">
    <div class="slide-title abs"><div class="t1">ADVENTURES</div><div class="t2">KAYAKING</div></div>
    <div class="slide-quote abs">“Vantor rocks all its events are well organised and enjoyable” !<span class="by">-Mara Ellison</span></div>
    <div class="dots abs"><i></i><i></i><i></i><i></i></div>
  </div>

  <svg class="ribbon abs" width="330" height="52" viewBox="0 0 330 52">
    <polygon points="0,8 36,8 36,44 14,44 24,26" fill="#3a3b41"/>
    <polygon points="330,8 294,8 294,44 316,44 306,26" fill="#3a3b41"/>
    <polygon points="26,0 304,0 304,40 26,40" fill="#4a4b52"/>
  </svg>
  <div class="ribbon-text abs">FREE MEMBERSHIP</div>

  <div class="offer-frame abs"></div>
  <div class="offer-photo abs" role="img" aria-label="Climber on a rock face above a blue sky"></div>
  <div class="offer-badge abs"></div>
  <div class="offer-text abs">INVITES<br>EVENTS &amp; ADVENTURES</div>
  <div class="arrow l abs"><svg width="12" height="16"><polygon points="12,0 0,8 12,16" fill="#c8101a"/></svg></div>
  <div class="arrow r abs"><svg width="12" height="16"><polygon points="0,0 12,8 0,16" fill="#c8101a"/></svg></div>
  <div class="value abs">value<br>$65</div>

  <form class="join-form">
    <label class="abs" style="left:635px;top:306px">NAME</label>
    <div class="field abs" style="left:710px;top:311px"></div>
    <label class="abs" style="left:635px;top:336px">EMAIL</label>
    <div class="field abs" style="left:711px;top:339px"></div>
    <div class="join-btn abs">JOIN NOW</div>
  </form>
</section>

<section class="promos abs">
  <article class="card-pt abs">
    <h3>PERSONAL<br>TRAINING</h3>
    <div class="figure abs" role="img" aria-label="Trainer stretching a client on the floor"></div>
    <p>Free<br>initial consult<br>1 on 1<br>session<br>(valued $80)</p>
    <div class="unl">Unlimited classes</div>
  </article>
  <article class="card-gf abs">
    <h3>GROUP<br>FITNESS</h3>
    <div class="gf-pass abs"><span>INTRO PASS</span><b>$25 FOR 7 DAYS</b></div>
  </article>
  <article class="card-bc abs">
    <div class="bc-soon abs">STARTS SOON<small>LIMITED SEATS</small></div>
    <div class="bc-icon abs" style="left:108px"></div>
    <div class="bc-icon abs" style="left:170px"></div>
    <div class="bc-title abs">BOOT CAMP</div>
  </article>
</section>

<section class="about abs">
  <h2>Personal Trainers in Brisbane</h2>
  <div class="about-copy abs">
    <p>If you are exercising and have committed a good chunk of time into your fitness, you want to make sure you get the best returns possible. This is where a personal trainer can help. In personal training sessions you will be pushed to achieve your personal best, meaning that you get the best results, both physically and mentally, from your fitness training.</p>
    <p>For those that are new to exercising, it can be difficult to know where to begin. Having a personal trainer on board will give you the guidance and support that you need. Those that enlist the help of a personal trainer often find that they achieve much better results than those that go it alone, and often in a much shorter space of time.</p>
  </div>
  <div class="video abs">
    <div class="video-frame" role="img" aria-label="Trainer guiding a man on a chest press machine in a gym"></div>
    <div class="play abs"><svg width="18" height="20"><polygon points="0,0 18,10 0,20" fill="#777"/></svg></div>
    <div class="controls abs"><svg width="8" height="9"><polygon points="0,0 8,4.5 0,9" fill="#1d4f7a"/></svg><span class="bar"></span><span>0:00 / 0:00</span></div>
  </div>
</section>

<footer class="site-footer abs"></footer>
</body>
</html>
```